Design Business Card & Electronic Word Document Stationary

Hi thanks for playing business card design wheel of fortune with me. :D

Please see the attached Word doc with very detailed instructions on this double-sided 2 or 3 color business card design with matching Microsoft Word online stationary design (letterhead and fax cover sheet).

All the business card content and colors to use are provided in the specs, the color and layout of the design is the only thing you're collarborating with me on doing with this contest project please note. I also provided a couple dozen modern business card examples in the specs as well, to better help your odds on winning the bid to put you on the right path on what I'm looking for design wise.

Thanks so much and good luck to you.

```html
<!DOCTYPE html>
<html lang="en">
<head>
<meta charset="utf-8">
<title>Roaming Wrench – Business Cards</title>
<link rel="stylesheet" href="https://fonts.googleapis.com/css2?family=Varela+Round&family=Arimo:wght@400;700&display=swap">
<style>
  :root {
    --stage: #2b2c2f;
    --navy: #2d3f7c;
    --navy-deep: #1f2d5e;
    --navy-light: #3d529a;
    --paper: #f1f1ef;
    --paper-grey: #e4e4e2;
    --teal: #1f7f9a;
    --white: #ffffff;
    --orange: #f29a2e;
  }
  * { box-sizing: border-box; margin: 0; padding: 0; }
  html, body { width: 1200px; height: 780px; overflow: hidden; }
  body { background: var(--stage); position: relative; font-family: "Arimo", sans-serif; }

  .card { position: absolute; width: 620px; height: 355px; overflow: hidden; box-shadow: 0 10px 24px rgba(0,0,0,.45); }
  .card--back { left: 50px; top: 38px; background: var(--paper-grey); }
  .card--front { left: 530px; top: 387px; background: var(--paper); }

  /* back side */
  .back__panel {
    position: absolute; left: 215px; top: 0; right: 0; bottom: 0;
    background: linear-gradient(135deg, var(--navy-light), var(--navy) 55%, var(--navy-deep));
  }
  .back__edge { position: absolute; left: 0; top: 0; width: 28px; height: 100%; background: var(--navy); }
  .back__copy {
    position: absolute; left: 235px; top: 20px; width: 300px;
    color: var(--white); font-size: 10.5px; line-height: 1.32; text-align: center;
  }
  .back__copy p + p { margin-top: 16px; }
  .back__art { position: absolute; right: 18px; width: 52px; height: 40px; border-radius: 6px; }
  .back__art--car { top: 40px; background: linear-gradient(135deg, #7a6fd0, #3a2f86); }
  .back__art--wheel { top: 135px; width: 46px; height: 46px; border-radius: 50%; background: radial-gradient(circle, #d9dde3 30%, #4aa7c9 70%); }
  .back__art--tablet { top: 230px; background: linear-gradient(135deg, #e7e7ea, #4f78a9); }

  /* brand block */
  .brand { position: absolute; display: flex; flex-direction: column; align-items: center; gap: 10px; }
  .brand__disc { width: 110px; height: 110px; border-radius: 50%; background: var(--white); }
  .brand__name { font-family: "Varela Round", sans-serif; font-size: 20px; color: var(--navy); letter-spacing: .5px; }
  .card--back .brand { left: 45px; top: 100px; }
  .card--front .brand { left: 45px; top: 100px; }
  .card--front .brand__name { color: var(--white); }

  /* front side */
  .front__band { position: absolute; left: 0; top: 0; width: 235px; height: 100%; background: linear-gradient(135deg, var(--navy-light), var(--navy-deep)); }
  .front__strip { position: absolute; right: 0; top: 0; width: 22px; height: 100%; background: var(--navy); }
  .front__title {
    position: absolute; left: 255px; top: 40px; width: 340px; text-align: center;
    font-family: "Varela Round", sans-serif; font-weight: 400; color: var(--teal); font-size: 19px; line-height: 1.3;
  }
  .front__contacts {
    position: absolute; left: 255px; top: 135px; width: 340px; list-style: none; text-align: center;
    color: var(--teal); font-family: "Varela Round", sans-serif; font-size: 13.5px; line-height: 1.32;
  }
</style>
</head>
<body>

<section class="card card--back" aria-label="Card back">
  <div class="back__edge"></div>
  <div class="back__panel"></div>
  <div class="brand">
    <div class="brand__disc"></div>
    <span class="brand__name">Roaming Wrench</span>
  </div>
  <div class="back__copy">
    <p>I can install custom LED and HID interior or exterior lights, video &amp; audio systems, backup cameras, GPS systems, car alarms, radar detectors, spoilers, cold air intake systems, remote starters, keyless entry, door pops, push button engine starters, dashboard gauge clusters, media player &amp; wireless integrations, body &amp; lift kits, scissor doors, custom engine harnesses or anything else you can imagine.</p>
    <p>I've worked on everything from fire trucks, tractors, food and catering trailers, buses, RV's, luxury, domestic and foreign vehicles, classic hot rods and muscle cars.</p>
    <p>I can install and repair anything in your vehicles starting, charging, heating and cooling, fuel, engine, suspension, steering and transmission systems. I can replace any type of belts, hoses, filters, fluids, switches, sensors, relays, fuses or wiring. Sorry I don't do transmission or engine rebuilds or replacements.</p>
  </div>
  <div class="back__art back__art--car" role="img" aria-label="Illustration of a purple sports car"></div>
  <div class="back__art back__art--wheel" role="img" aria-label="Illustration of a chrome alloy wheel"></div>
  <div class="back__art back__art--tablet" role="img" aria-label="Illustration of a hand holding a tablet"></div>
</section>

<section class="card card--front" aria-label="Card front">
  <div class="front__band"></div>
  <div class="front__strip"></div>
  <div class="brand">
    <div class="brand__disc"></div>
    <span class="brand__name">Roaming Wrench</span>
  </div>
  <h1 class="front__title">Nationwide Mobile Mechanic &amp;<br>Vehicle Customization Expert</h1>
  <ul class="front__contacts">
    <li>555-014-2207</li>
    <li>dale@roamingwrench.com</li>
    <li>www.roamingwrench.com</li>
    <li>www.chirpline.net/roamingwrench</li>
    <li>www.vidreel.net/roamingwrench</li>
    <li>www.pinwall.net/roamingwrench</li>
    <li>www.friendcircle.net/roamingwrench</li>
  </ul>
</section>

</body>
</html>
```